Training company needs a Quick Reference Card design

We have draft skeleton of the design and most of the text. But we need a designer to take it the rest if the way.
I have designed a 2 page quick reference card - it is meant to be a 2-sided document. The first page is portrait, the back page can either be portrait or landscape, I'm not too concerned, whichever fits best.
Section called 'Maps' on front, a map is a collection of documents (like a manual), a topic is a document (like a page or section of a manual) and a block is a section of a document. The graphic is mean to illustrate the hierarchy but essentially a map is a big document with smaller documents in it.
Please use the company's logo colors to differentiate the different sections with minimal/ highlight only use of the darkest color, preferably.
Please use the icons for the corresponding Information types in the chart of the back - except please re-design the icons color scheme to match the company's logo/website colors.

Target Market(s)

Technical writers, after attending our training course, as an ongoing resource for them

Industry/Entity Type

It Company

Font styles to use
Sans Serif

Requirements
Must have
• Must adhere to look and feel of brand/ website. www.lumarockwise.com
Nice to have
• Please keep the design modern and slick looking, not too busy, easy to read

```html
<!DOCTYPE html>
<html lang="en">
<head>
<meta charset="utf-8">
<title>Quick Reference Card</title>
<link rel="stylesheet" href="https://fonts.googleapis.com/css2?family=Montserrat:wght@400;500;600;700&display=swap">
<style>
  :root{
    --blue:#1d9ad6;
    --navy:#2b2c8f;
    --ink:#1e1e1e;
    --panel:#e4f2fb;
    --line:#6cbbe6;
    --frame:#444;
    --white:#fff;
  }
  *{margin:0;padding:0;box-sizing:border-box}
  html,body{width:1200px;height:682px;overflow:hidden;background:var(--white)}
  body{font-family:"Montserrat",Arial,sans-serif;color:var(--ink)}
  .stage{position:absolute;left:0;top:0;width:1500px;height:853px;transform:scale(.8);transform-origin:0 0}
  .abs{position:absolute}

  /* front page */
  .page-front{position:absolute;left:18px;top:18px;width:632px;height:817px;border:1px solid var(--frame)}
  .brand{position:absolute;left:35px;top:42px;display:flex;align-items:center;gap:10px}
  .brand-dot{width:56px;height:56px;border-radius:50%;background:var(--navy)}
  .brand-name{font-weight:700;font-size:17px;color:var(--navy)}
  .card-title{position:absolute;left:279px;top:52px;font-size:29px;font-weight:500;color:var(--blue)}

  .panel{position:absolute;background:var(--panel);border:1.5px solid var(--line);border-radius:6px}
  .tab{position:absolute;height:23px;background:var(--navy);color:var(--white);font-weight:600;font-size:13px;line-height:23px;padding-left:20px;border-radius:4px 4px 0 0;white-space:nowrap}
  .body-text{font-size:10.8px;line-height:14.5px;letter-spacing:-.2px}
  .sub-head{font-size:12.5px;font-weight:500;color:var(--blue);margin-bottom:6px;letter-spacing:0;white-space:nowrap}

  .map-diagram{position:absolute;left:9px;top:8px;width:232px;height:143px;background:var(--white);border:1.5px solid var(--line);border-radius:4px}
  .map-label{position:absolute;left:100px;top:10px;font-size:13px}
  .topic-box{position:absolute;top:38px;width:101px;height:91px;border:1.5px solid var(--line)}
  .topic-box .name{text-align:center;font-size:11.5px;margin-top:6px}
  .mini{position:absolute;left:7px;width:85px;height:20px;border:1.5px solid var(--line);text-align:center;font-size:10px;line-height:17px;color:var(--blue);white-space:nowrap}
  .defs{position:absolute;left:257px;top:10px;width:292px}
  .defs p{margin-bottom:8px}
  .defs b{color:var(--blue);font-weight:600}

  .rule-col{position:absolute;top:10px}
  .center{text-align:center}

  /* back page */
  .page-back{position:absolute;left:666px;top:110px;width:819px;height:633px;border:1px solid var(--frame)}
  .grid{position:absolute;left:36px;width:746px;display:grid;grid-template-columns:79px repeat(5,133.4px)}
  .grid.band{background:var(--panel)}
  .cell{font-size:10.8px;line-height:14.5px;letter-spacing:-.2px;padding:6px 7px 0 9px}
  .row-label{font-size:12px;font-weight:600;line-height:16px;text-align:center;display:flex;align-items:center;justify-content:center;padding:0}
  .type-head{display:flex;flex-direction:column;align-items:center;justify-content:flex-end;padding-bottom:8px;color:var(--blue);font-size:15px;font-weight:500}
  .type-head svg{margin-bottom:6px}
  .col-rule{position:absolute;top:36px;width:1px;height:574px;background:var(--line)}
</style>
</head>
<body>
<div class="stage">

  <section class="page-front">
    <div class="brand"><span class="brand-dot"></span><span class="brand-name">LUMAROCKWISE</span></div>
    <h1 class="card-title">Quick Reference Card</h1>

    <div class="panel" style="left:35px;top:123px;width:560px;height:159px">
      <div class="map-diagram">
        <svg class="abs" style="left:0;top:0" width="232" height="40">
          <path d="M60 38V18H98M140 18H168V38" fill="none" stroke="#6cbbe6" stroke-width="1.5"/>
        </svg>
        <div class="map-label">Map</div>
        <div class="topic-box" style="left:10px">
          <div class="name">Topic</div>
          <div class="mini" style="top:30px">Primary Block</div>
          <div class="mini" style="top:61px">Block</div>
        </div>
        <div class="topic-box" style="left:119px">
          <div class="name">Topic</div>
          <div class="mini" style="top:30px">Primary Block</div>
          <div class="mini" style="top:61px">Block</div>
        </div>
      </div>
      <div class="defs body-text">
        <p>A <b>map</b> is a file that organizes topics into structured collections of information. Maps specify hierarchy and relationships among topics.</p>
        <p>A <b>topic</b> is a group of related blocks with a title. Use the chunking principle to group together relevant blocks.</p>
        <p>A <b>block</b> is a bite-sized chunk of information about one main idea that allows the writer to organize the material into logical sections.</p>
      </div>
    </div>

    <div class="tab" style="left:35px;top:301px;width:183px">General Writing Rules</div>
    <div class="panel" style="left:35px;top:328px;width:560px;height:117px">
      <div class="rule-col body-text" style="left:18px;width:178px">
        <div class="sub-head">EFFECTIVE SENTENCES</div>
        One main agent, action &amp; outcome. Use active voice and simplest tense possible. No more than 7 sentences per paragraph. Use lists and tables.
      </div>
      <div class="rule-col body-text" style="left:206px;width:164px">
        <div class="sub-head">SPECIAL CHARACTERS</div>
        Avoid special characters, spell out words instead. Remove parentheses, colon and dashes. Avoid using quotation marks and slashes.
      </div>
      <div class="rule-col body-text" style="left:378px;width:172px">
        <div class="sub-head">PLAIN LANGUAGE</div>
        Write in short sentences. Provide useful titles. Use clear familiar words. Avoid excess words. Be consistent.
      </div>
    </div>

    <div class="tab" style="left:35px;top:465px;width:323px">3 Questions to Ask Before You Start Writing</div>
    <div class="panel body-text" style="left:35px;top:491px;width:323px;height:94px;padding:11px 8px 0 13px">
      <p style="margin-bottom:8px">1. What is the purpose of this information?</p>
      <p style="margin-bottom:8px">2. What is the desired user response of this information?</p>
      <p>3. Who is the audience?</p>
    </div>

    <div class="tab" style="left:368px;top:465px;width:227px;padding-left:32px">2 Types of Language Arts</div>
    <div class="panel body-text center" style="left:368px;top:491px;width:227px;height:94px;padding-top:10px">
      <div class="sub-head" style="margin:0">LAFI</div>
      <p>Language Arts for Information</p>
      <div class="sub-head" style="margin:12px 0 0">LAFPR</div>
      <p>Language Arts of Personal Reponse</p>
    </div>

    <div class="tab" style="left:35px;top:604px;width:183px">4 Cognitive Principles</div>
    <div class="panel" style="left:35px;top:631px;width:560px;height:150px">
      <div class="rule-col body-text" style="left:16px;top:9px;width:265px">
        <div class="sub-head">Consistency</div>
        Use similar terms and structures. Pick a term and stick with it. Use the same sequence of blocks. Use consistent styles.
      </div>
      <div class="rule-col body-text" style="left:289px;top:9px;width:262px">
        <div class="sub-head">Chunking</div>
        Maximum of nine (7 +/- 2) items in a list, rows in a table, blocks in a topic, or topics in a map.
      </div>
      <div class="rule-col body-text" style="left:16px;top:84px;width:265px">
        <div class="sub-head">Relevance</div>
        Group similar items together. Separate relevance? Separate block. Irrelevant? Delete it.
      </div>
      <div class="rule-col body-text" style="left:289px;top:84px;width:262px">
        <div class="sub-head">Titling</div>
        Name everything. Name every block, every topic, every map and every table column
      </div>
    </div>
  </section>

  <section class="page-back">
    <div class="grid" style="top:36px;height:80px">
      <div></div>
      <div class="type-head">
        <svg width="20" height="36" viewBox="0 0 20 36"><circle cx="12" cy="4" r="3.5" fill="#1d9ad6"/><path d="M6 12h9l-4 18h4v4H3v-4h3l3-14H5z" fill="#2b2c8f"/></svg>Reference</div>
      <div class="type-head">
        <svg width="36" height="36" viewBox="0 0 36 36"><g stroke="#1d9ad6" stroke-width="2.5" stroke-linecap="round"><path d="M18 2v4M5 8l3 3M31 8l-3 3M2 19h4M30 19h4"/></g><circle cx="18" cy="18" r="8" fill="#2b2c8f"/><rect x="14" y="26" width="8" height="6" rx="1.5" fill="#1d9ad6"/></svg>Concept</div>
      <div class="type-head">
        <svg width="30" height="36" viewBox="0 0 30 36"><g fill="#2b2c8f"><rect x="5" y="5" width="4.5" height="18" rx="2.2"/><rect x="10.5" y="1" width="4.5" height="20" rx="2.2"/><rect x="16" y="2" width="4.5" height="20" rx="2.2"/><rect x="21.5" y="6" width="4.5" height="17" rx="2.2"/><rect x="5" y="16" width="21" height="18" rx="7"/></g></svg>Principle</div>
      <div class="type-head">
        <svg width="38" height="36" viewBox="0 0 38 36"><circle cx="14" cy="13" r="9" fill="none" stroke="#2b2c8f" stroke-width="5" stroke-dasharray="4 3"/><circle cx="14" cy="13" r="3" fill="#2b2c8f"/><circle cx="28" cy="26" r="6" fill="none" stroke="#1d9ad6" stroke-width="4" stroke-dasharray="3 2.3"/><circle cx="28" cy="26" r="2" fill="#1d9ad6"/></svg>Process</div>
      <div class="type-head">
        <svg width="28" height="36" viewBox="0 0 28 36"><rect x="2" y="5" width="24" height="29" rx="2" fill="none" stroke="#2b2c8f" stroke-width="3"/><rect x="9" y="2" width="10" height="6" rx="1.5" fill="#2b2c8f"/><path d="M8 20l4.5 4.5L20 15" fill="none" stroke="#1d9ad6" stroke-width="3"/></svg>Task</div>
    </div>

    <div class="grid band" style="top:116px;height:58px">
      <div class="row-label">Definition</div>
      <div class="cell">Describes things the reader needs to know</div>
      <div class="cell">Explains things the reader needs to understand</div>
      <div class="cell">Advises the reader what they need to do or not do and when</div>
      <div class="cell">Demonstrates to the reader how things work</div>
      <div class="cell">Instructs the reader on how to do things</div>
    </div>

    <div class="grid" style="top:174px;height:107px">
      <div class="row-label">Type of<br>authoring<br>models</div>
      <div class="cell">Sentences/phrases<br>Lists<br>Tables<br>Diagrams<br>Part-description<br>Part-function</div>
      <div class="cell">Sentences/phrases<br>Lists<br>Tables<br>Diagrams<br>Illustrations</div>
      <div class="cell">Sentences/phrases<br>Lists<br>Tables<br>Decision tree<br>Graphic</div>
      <div class="cell">Sentences/phrases<br>Stage ordered list<br>When/the<br>Condition tree<br>Graphic example</div>
      <div class="cell">Sentences/phrases<br>Lists<br>If/then decision<br>Tree<br>Graphic example</div>
    </div>

    <div class="grid band" style="top:281px;height:116px">
      <div class="row-label">Titling<br>best<br>practices</div>
      <div class="cell">Describes the item and anything that differentiates it from other items</div>
      <div class="cell">Use the plural form of the noun, if one exists. Don’t add additional words such as “About”, “What”, “is”, or “Definition”</div>
      <div class="cell">Identifies the principle and expresses the gravity of the principle. Formula = Gravity + Principle, or Principle + Gravity</div>
      <div class="cell">Human processes: Gerund of verb + noun “Grooming a dog”. System processes: Use “How (item) works” Ex “How engines work”</div>
      <div class="cell">Starts with an imperative verb, do not use gerund. “Mow the lawn” “Boil and egg” “Register for a course”</div>
    </div>

    <div class="grid" style="top:397px;height:47px">
      <div class="row-label">Primary<br>block title</div>
      <div class="cell" style="padding-top:15px">Introduction</div>
      <div class="cell" style="padding-top:15px">Definition</div>
      <div class="cell" style="padding-top:15px">Statement</div>
      <div class="cell" style="padding-top:15px">Summary</div>
      <div class="cell" style="padding-top:15px">Purpose</div>
    </div>

    <div class="grid band" style="top:444px;height:86px">
      <div class="row-label">Primary<br>block<br>content</div>
      <div class="cell">Provide a description of the reference topic and how it would be used</div>
      <div class="cell">Provide the exact meaning of the concept</div>
      <div class="cell">Provide a high-level summary of the principle</div>
      <div class="cell">Provide a short explanation of the purpose of the process, or the need for the process</div>
      <div class="cell">Provide an explanation of why or when the reader would use the task</div>
    </div>

    <div class="grid" style="top:530px;height:80px">
      <div class="row-label">Tips and<br>examples</div>
      <div></div><div></div><div></div><div></div><div></div>
    </div>

    <div class="col-rule" style="left:115px"></div>
    <div class="col-rule" style="left:248px"></div>
    <div class="col-rule" style="left:382px"></div>
    <div class="col-rule" style="left:515px"></div>
    <div class="col-rule" style="left:648px"></div>
  </section>

</div>
</body>
</html>
```